Business Card Design

I need a business card for my tutoring service. Key elements on front are its contact details and visual appeal with these three points: All aspects of literacy and numeracy, 'Bright Pathways Support' provider and Prep-readiness sessions
Updates

contact me by email on korawen7@mailtrove.net as I'm having issues with other address at times. Thanks

:) 

Target Market(s)

People with children

Industry/Entity Type

Tutoring

Contact Information for Business Card

Tessa Brindle Educational Consultant
17 Quillon Grove
Tarrowin 4821
0487 316 912

Requirements
Nice to have
• Something related to education. On the back of the card, my business name and phone number again, along with: spelling, reading, writing, comprehension, oral language, listening skills

```html
<!DOCTYPE html>
<html lang="en">
<head>
<meta charset="utf-8">
<title>Tessa Brindle's Tutoring Service – Business Card</title>
<link href="https://fonts.googleapis.com/css2?family=Bebas+Neue&display=swap" rel="stylesheet">
<style>
  :root {
    --bg: #e9e6e1;
    --taupe: #6e6462;
    --cream: #fbfaea;
    --pink: #ef5a72;
    --blue: #5cc3ec;
    --ink: #5a5250;
    --white: #ffffff;
  }
  * { box-sizing: border-box; margin: 0; padding: 0; }
  html, body {
    width: 1200px; height: 800px; overflow: hidden;
    background: var(--bg);
    font-family: "Bebas Neue", "Oswald", sans-serif;
  }
  .sheet {
    position: relative; width: 1200px; height: 800px;
  }
  .card {
    position: absolute; top: 245px;
    width: 540px; height: 310px;
    background: var(--cream);
    overflow: hidden;
    box-shadow: 0 6px 18px rgba(0,0,0,0.15);
  }
  .card--front { left: 40px; }
  .card--back { left: 620px; }
  .card__shape { position: absolute; inset: 0; width: 100%; height: 100%; }
  .card__text { position: absolute; line-height: 1; }

  /* Front */
  .front-name { left: 30px; top: 28px; color: var(--white); font-size: 32px; letter-spacing: 1px; }
  .rule { display: block; height: 3px; margin-top: 6px; }
  .rule--pink { background: var(--pink); }
  .rule--blue { background: var(--blue); }
  .rule-pair { display: flex; gap: 0; margin-top: 5px; }
  .rule-pair span { height: 3px; }
  .front-role { left: 30px; top: 84px; color: var(--white); font-size: 17px; letter-spacing: 0.5px; }
  .front-rules { left: 30px; top: 72px; width: 170px; }
  .accent-bar { position: absolute; left: 30px; top: 150px; width: 22px; height: 82px; background: var(--pink); }
  .front-contact { left: 68px; top: 158px; color: var(--white); font-size: 17px; line-height: 1.45; letter-spacing: 0.5px; }
  .front-service { left: 280px; top: 168px; font-size: 42px; letter-spacing: 0.5px; }
  .pink { color: var(--pink); }
  .blue { color: var(--blue); }
  .front-points { left: 282px; top: 214px; color: var(--ink); font-size: 16px; line-height: 1.2; letter-spacing: 0.4px; }

  /* Back */
  .back-title { left: 178px; top: 46px; font-size: 54px; letter-spacing: 1px; }
  .back-sub { left: 232px; top: 102px; color: var(--ink); font-size: 34px; letter-spacing: 1px; }
  .back-skills { left: 184px; top: 146px; color: var(--pink); font-size: 14px; letter-spacing: 0.4px; }
  .back-rules { left: 300px; top: 172px; width: 120px; }
  .back-phone { left: 300px; top: 190px; color: var(--ink); font-size: 20px; letter-spacing: 1px; }
</style>
</head>
<body>
<main class="sheet">

  <section class="card card--front" aria-label="Card front">
    <svg class="card__shape" viewBox="0 0 540 310" aria-hidden="true">
      <path d="M0 0 H240 C205 55 225 105 252 140 C280 180 235 240 205 310 H0 Z" fill="var(--taupe)"/>
      <path d="M240 0 C205 55 225 105 252 140 C280 180 235 240 205 310" fill="none" stroke="var(--blue)" stroke-width="2" transform="translate(4 0)"/>
    </svg>
    <h1 class="card__text front-name">Tessa Brindle</h1>
    <div class="card__text front-rules">
      <div class="rule-pair"><span style="width:50%;background:var(--pink)"></span><span style="width:50%;background:var(--blue)"></span></div>
    </div>
    <p class="card__text front-role">Educational Consultant</p>
    <div class="accent-bar"></div>
    <address class="card__text front-contact" style="font-style:normal">
      0487 316 912<br>
      17 Quillon Grove<br>
      Tarrowin 4821
    </address>
    <h2 class="card__text front-service"><span class="pink">Tutoring</span> <span class="blue">Service</span></h2>
    <ul class="card__text front-points" style="list-style:none">
      <li>All aspects of literacy and numeracy</li>
      <li>Bright Pathways Support</li>
      <li>Prep-readiness sessions</li>
    </ul>
  </section>

  <section class="card card--back" aria-label="Card back">
    <svg class="card__shape" viewBox="0 0 540 310" aria-hidden="true">
      <path d="M0 0 H175 C140 45 170 90 150 130 C128 175 120 240 95 310 H0 Z" fill="var(--taupe)"/>
    </svg>
    <h2 class="card__text back-title"><span class="blue">Tessa</span> <span class="pink">Brindle's</span></h2>
    <p class="card__text back-sub">Tutoring Service</p>
    <p class="card__text back-skills">Spelling, reading, writing, comprehension, oral language, listening skills</p>
    <div class="card__text back-rules">
      <div class="rule-pair"><span style="width:50%;background:var(--pink)"></span><span style="width:50%;background:var(--blue)"></span></div>
    </div>
    <p class="card__text back-phone">0487 316 912</p>
  </section>

</main>
</body>
</html>
```